front and back labels on a single sheet.

Vodka label design
Vodka is a colourless liquor. This vodka is tasteless and with no flavour.

FRONT LABEL
"FROST TALLY" is the brand name . it should be as big as possible.
below that " Only vodka made from sustainable means"
Remaining details to be copied from attached file.
Back Label
Details attached.

Colors
00AB8E
00BBA5
67D7C9
C6EFE9
E9F9F6

```html
<!DOCTYPE html>
<html lang="en">
<head>
<meta charset="utf-8">
<title>Frost Tally Vodka – Front and Back Labels</title>
<link href="https://fonts.googleapis.com/css2?family=Bebas+Neue&family=Montserrat:wght@400;500;600;700;800&family=Roboto:wght@400;700&display=swap" rel="stylesheet">
<style>
  :root {
    --teal-deep: #00AB8E;
    --teal: #00BBA5;
    --teal-light: #67D7C9;
    --mint: #C6EFE9;
    --mint-pale: #E9F9F6;
    --silver: #eceeef;
    --silver-dark: #d6d9db;
    --ink: #2b2b2b;
    --leaf: #2f8f2a;
    --warn: #d8232a;
    --sheet: #f4f4f2;
  }
  * { box-sizing: border-box; margin: 0; padding: 0; }
  html, body { width: 1070px; height: 1200px; overflow: hidden; }
  body { background: var(--sheet); font-family: "Montserrat", sans-serif; position: relative; }

  .label {
    position: absolute; top: 270px; width: 462px; height: 662px; overflow: hidden;
    background: linear-gradient(180deg, var(--silver-dark) 0%, var(--silver) 18%, #f6f7f7 100%);
    box-shadow: 0 2px 10px rgba(0,0,0,.12);
  }
  .label--front { left: 55px; }
  .label--back { left: 553px; }
  .label__bg { position: absolute; inset: 0; }

  /* front */
  .brand-mark { position: absolute; top: 40px; left: 0; width: 100%; text-align: center; }
  .brand-mark__row { display: inline-flex; align-items: center; gap: 6px; }
  .brand-mark__dot { width: 14px; height: 14px; border-radius: 50%; background: var(--leaf); }
  .brand-mark__name { font-family: "Montserrat", sans-serif; font-weight: 700; font-size: 15px; color: var(--leaf); letter-spacing: .5px; }
  .brand-mark__tagline { font-size: 5px; color: #666; text-transform: uppercase; letter-spacing: .4px; margin-top: 3px; }

  .title-panel {
    position: absolute; left: 42px; top: 146px; width: 418px; height: 372px;
    background: linear-gradient(160deg, #fafafa 0%, #e9ebec 60%, #f7f7f7 100%);
  }
  .title-panel__name {
    position: absolute; left: 0; top: 8px; width: 100%; text-align: center;
    font-family: "Bebas Neue", sans-serif; color: var(--teal-deep);
    font-size: 188px; line-height: 152px; letter-spacing: 2px;
  }
  .title-panel__claim {
    position: absolute; left: 0; bottom: 22px; width: 100%; text-align: center;
    font-family: "Bebas Neue", sans-serif; color: var(--teal-deep); font-size: 25px; letter-spacing: .3px;
  }
  .grade {
    position: absolute; top: 556px; left: 0; width: 100%;
    display: flex; align-items: center; gap: 14px; padding: 0 0;
    font-family: "Bebas Neue", sans-serif; color: #fff; font-size: 22px; letter-spacing: 2px;
  }
  .grade::before, .grade::after { content: ""; flex: 1; height: 1px; background: rgba(255,255,255,.75); }
  .specs {
    position: absolute; top: 604px; left: 26px; right: 26px;
    display: flex; justify-content: space-between;
    font-family: "Bebas Neue", sans-serif; color: #fff; font-size: 34px; letter-spacing: 2px;
  }

  /* back */
  .story {
    position: absolute; top: 122px; left: 24px; right: 24px; text-align: center;
    font-size: 11.4px; line-height: 19px; color: var(--ink); font-weight: 500; text-transform: uppercase;
  }
  .rule { position: absolute; left: 44px; right: 24px; height: 1px; background: #9a9a9a; }
  .rule--top { top: 224px; }
  .rule--bottom { top: 333px; }

  .compliance { position: absolute; top: 244px; left: 44px; right: 30px; display: flex; align-items: center; gap: 20px; }
  .warning { display: flex; align-items: center; width: 250px; height: 52px; border: 1.5px solid var(--warn); border-radius: 5px; background: #fff; }
  .warning__icon { width: 50px; height: 50px; margin-left: -2px; border-radius: 50%; background: #eee; border: 4px solid var(--warn); flex: none; }
  .warning__text { padding-left: 10px; font-family: "Roboto", sans-serif; font-size: 11px; line-height: 12px; color: #333; }
  .warning__title { font-family: "Montserrat", sans-serif; font-weight: 800; color: var(--warn); font-size: 11.5px; letter-spacing: .5px; margin-bottom: 2px; }
  .std-drink { width: 50px; }
  .recycle { width: 46px; text-align: center; font-size: 7px; font-weight: 700; color: #222; }

  .details { position: absolute; top: 350px; left: 42px; right: 20px; display: flex; }
  .details__col { font-size: 9.2px; line-height: 14px; color: #555; text-transform: uppercase; }
  .details__col--use { width: 150px; padding-right: 10px; }
  .details__col--maker { flex: 1; padding-left: 24px; border-left: 1px solid #777; margin-left: 10px; height: 84px; }
  .details__small { font-size: 7.5px; line-height: 10px; color: #222; margin-top: 6px; }
  .details__strong { font-weight: 600; color: #222; margin-top: 8px; }

  .source-band {
    position: absolute; top: 447px; left: 0; width: 100%; height: 34px;
    background: var(--teal-deep); color: #fff; text-align: center;
    font-weight: 800; font-size: 21px; line-height: 34px; letter-spacing: .3px;
  }
  .founder-portrait {
    position: absolute; left: 144px; top: 530px; width: 166px; height: 132px;
    background: linear-gradient(180deg, #f2f2f2 0%, #cfcfcf 100%);
  }
</style>
</head>
<body>

  <section class="label label--front" aria-label="Front label">
    <svg class="label__bg" width="462" height="662" viewBox="0 0 462 662" aria-hidden="true">
      <polygon points="462,50 462,662 0,662 0,392" fill="var(--teal)"/>
      <polygon points="462,50 462,300 160,420" fill="var(--teal-light)" opacity=".45"/>
      <polygon points="0,392 0,662 260,662" fill="var(--teal-deep)" opacity=".6"/>
      <polygon points="0,540 462,470 462,662 0,662" fill="var(--teal-deep)" opacity=".35"/>
    </svg>

    <div class="brand-mark">
      <div class="brand-mark__row"><span class="brand-mark__dot"></span><span class="brand-mark__name">VERDANT STILL</span></div>
      <div class="brand-mark__tagline">Spirits distilled with pure natural care</div>
    </div>

    <div class="title-panel">
      <h1 class="title-panel__name">FROST<br>TALLY</h1>
      <p class="title-panel__claim">Only vodka made from sustainable means</p>
    </div>

    <p class="grade">Premium quality vodka</p>
    <div class="specs"><span>50%</span><span>750ml</span></div>
  </section>

  <section class="label label--back" aria-label="Back label">
    <svg class="label__bg" width="462" height="662" viewBox="0 0 462 662" aria-hidden="true">
      <polygon points="462,366 462,447 250,447" fill="var(--teal)"/>
      <polygon points="462,481 462,662 70,662 300,481" fill="var(--teal)"/>
      <polygon points="462,560 462,662 260,662" fill="var(--teal-deep)" opacity=".45"/>
    </svg>

    <p class="story">The only vodka in the whole world which has unique 5 spices, and distilled 3+1 times. In addition this is the only vodka made from natural rainwater &amp; solar power, thus making it the only vodka that is sustainably manufactured.</p>

    <div class="rule rule--top"></div>
    <div class="compliance">
      <div class="warning">
        <div class="warning__icon" role="img" aria-label="Pregnancy warning pictogram"></div>
        <div class="warning__text">
          <div class="warning__title">PREGNANCY WARNING</div>
          Alcohol can cause lifelong<br>harm to your baby
        </div>
      </div>
      <svg class="std-drink" viewBox="0 0 50 56" role="img" aria-label="27 standard drinks approx">
        <polygon points="2,2 48,2 42,54 8,54" fill="#fff" stroke="#111" stroke-width="2"/>
        <polygon points="6,16 44,16 40,44 10,44" fill="#111"/>
        <text x="25" y="9" font-size="5.5" font-weight="700" text-anchor="middle" font-family="Montserrat, sans-serif">STANDARD</text>
        <text x="25" y="14.5" font-size="5.5" font-weight="700" text-anchor="middle" font-family="Montserrat, sans-serif">DRINK</text>
        <text x="25" y="39" font-size="22" font-weight="800" fill="#fff" text-anchor="middle" font-family="Montserrat, sans-serif">27</text>
        <text x="25" y="51" font-size="5" font-weight="700" text-anchor="middle" font-family="Montserrat, sans-serif">APPROX</text>
      </svg>
      <div class="recycle">
        <svg width="40" height="38" viewBox="0 0 40 38" aria-hidden="true">
          <polygon points="20,4 36,32 4,32" fill="none" stroke="#111" stroke-width="3" stroke-linejoin="round"/>
        </svg>
        GLASS
      </div>
    </div>
    <div class="rule rule--bottom"></div>

    <div class="details">
      <div class="details__col details__col--use">
        This vodka has to be taken chilled with ice cubes. Making cocktails with lime and orange is a wonderful experience.
        <div class="details__small">Contact at:<br>contact@verdantstill.com.au</div>
      </div>
      <div class="details__col details__col--maker">
        Fermented and distilled by:<br>Marlow T. Quinlan<br>at Verdant Still Pvt Ltd
        <div class="details__strong">Made in: Wattle Creek,<br>Victoria, Australia</div>
      </div>
    </div>

    <div class="source-band">MADE FROM SUGARCANE</div>
    <div class="founder-portrait" role="img" aria-label="Pencil sketch portrait of the distiller"></div>
  </section>

</body>
</html>
```